Business Card for Field Lotus-Eco Friendly Organic Clothing Brand

We are looking for an amazing business card for our eco friendly, organic clothing brand. We are thinking maybe a business card with a peel off sticker on the back, since our hanging clothing tag is a peel off sticker on the back. I will attach our hang tag so we can make sure we stay in line with our design. I've also attached a bag we are doing because I do like the scattered emblem look as well.

```html
<!DOCTYPE html>
<html lang="en">
<head>
<meta charset="utf-8">
<title>Field Lotus – Business Card</title>
<link href="https://fonts.googleapis.com/css2?family=Arimo:wght@400;700&family=Tinos:wght@700&display=swap" rel="stylesheet">
<style>
  :root {
    --canvas: #e9e6e3;
    --card-black: #161616;
    --card-white: #f6fbfa;
    --silver: #cfc8cd;
    --magenta: #e3157f;
    --army-green: #1d6b3c;
    --ink: #111111;
  }
  * { margin: 0; padding: 0; box-sizing: border-box; }
  html, body { width: 1200px; height: 780px; overflow: hidden; }
  body {
    background: var(--canvas);
    font-family: "Arimo", Arial, sans-serif;
    position: relative;
  }
  .card {
    position: absolute;
    top: 235px;
    width: 540px;
    height: 309px;
    border-radius: 4px;
    overflow: hidden;
    box-shadow: 0 6px 18px rgba(0,0,0,0.25);
  }
  .card--front { left: 40px; background: var(--card-black); }
  .card--back { left: 620px; background: var(--card-white); }

  .brand {
    position: absolute;
    display: flex;
    align-items: center;
    gap: 14px;
    font-family: "Arimo", Arial, sans-serif;
    font-weight: 700;
    white-space: nowrap;
  }
  .brand__dot { width: 38px; height: 38px; border-radius: 50%; }
  .card--front .brand { left: 50%; top: 50%; transform: translate(-50%, -50%); font-size: 44px; color: var(--silver); }
  .card--front .brand__dot { background: #3a3a3a; width: 52px; height: 52px; }

  .back__top {
    position: absolute; left: 0; top: 0; width: 100%; height: 132px;
    background: var(--card-black);
  }
  .card--back .brand { right: 40px; top: 46px; font-size: 34px; color: var(--magenta); }
  .card--back .brand__dot { background: #5f6b3a; }

  .stripe { position: absolute; left: 0; width: 100%; }
  .stripe--pink-top { top: 132px; height: 5px; background: var(--magenta); }
  .stripe--green-top { top: 140px; height: 3px; background: var(--army-green); }
  .stripe--green-bottom { top: 285px; height: 3px; background: var(--army-green); }
  .stripe--pink-bottom { top: 291px; height: 5px; background: var(--magenta); }
  .back__foot { position: absolute; left: 0; top: 296px; width: 100%; height: 13px; background: var(--card-black); }

  .person { position: absolute; left: 26px; top: 168px; color: var(--ink); }
  .person__name { font-family: "Tinos", "Times New Roman", serif; font-weight: 700; font-size: 26px; line-height: 1.05; }
  .person__title { font-size: 17px; line-height: 1.2; }

  .contacts {
    position: absolute; left: 255px; top: 160px;
    border-left: 1.5px solid var(--ink);
    padding-left: 8px;
    list-style: none;
  }
  .contact { display: flex; align-items: center; gap: 12px; height: 26px; font-size: 16px; color: var(--ink); }
  .contact__icon { width: 13px; height: 13px; flex: none; }
</style>
</head>
<body>

  <section class="card card--front">
    <div class="brand"><span class="brand__dot"></span>Field Lotus</div>
  </section>

  <section class="card card--back">
    <div class="back__top"></div>
    <div class="brand"><span class="brand__dot"></span>Field Lotus</div>
    <div class="stripe stripe--pink-top"></div>
    <div class="stripe stripe--green-top"></div>

    <div class="person">
      <p class="person__name">Dana Porter</p>
      <p class="person__title">Managing Director</p>
    </div>

    <ul class="contacts">
      <li class="contact">
        <svg class="contact__icon" viewBox="0 0 13 13"><rect width="13" height="13" fill="#111"/><path d="M4 3c-1 1-1 3 1 5s4 2 5 1l-1.5-1.5-1 .8c-1-.5-2-1.5-2.5-2.5l.8-1z" fill="#fff"/></svg>
        (555) 014-2290
      </li>
      <li class="contact">
        <svg class="contact__icon" viewBox="0 0 13 13"><rect width="13" height="13" fill="#111"/><path d="M6.5 2.5a2.6 2.6 0 0 1 2.6 2.6c0 2-2.6 5.2-2.6 5.2S3.9 7.1 3.9 5.1a2.6 2.6 0 0 1 2.6-2.6z" fill="#fff"/><circle cx="6.5" cy="5.1" r="1" fill="#111"/></svg>
        Coral Bend, FL&nbsp; 33012
      </li>
      <li class="contact">
        <svg class="contact__icon" viewBox="0 0 13 13"><rect width="13" height="13" fill="#111"/><circle cx="6.5" cy="6.5" r="3.8" fill="none" stroke="#fff" stroke-width="1"/><path d="M2.7 6.5h7.6M6.5 2.7c-2 2.5-2 5.1 0 7.6M6.5 2.7c2 2.5 2 5.1 0 7.6" fill="none" stroke="#fff" stroke-width=".8"/></svg>
        www.fieldlotus.com
      </li>
      <li class="contact">
        <svg class="contact__icon" viewBox="0 0 13 13"><rect width="13" height="13" fill="#111"/><rect x="2.5" y="4" width="8" height="5.5" fill="#fff"/><path d="M2.5 4l4 3 4-3" fill="none" stroke="#111" stroke-width=".9"/></svg>
        hello@fieldlotus.com
      </li>
    </ul>

    <div class="stripe stripe--green-bottom"></div>
    <div class="stripe stripe--pink-bottom"></div>
    <div class="back__foot"></div>
  </section>

</body>
</html>
```